Buch-/E-Book-Cover Pathways to Hire & Charm the Locals
Klares Design und rasche Umsetzung aller Änderungswünsche. Vielen Dank, gerne wieder.
Zielgruppe
Ich helfe internationalen Fachkräften Jobs in Deutschland zu finden. Meine Zielgruppe ist hochgebildet (97% mit Uni-Abschluss), spricht fließend englisch, ist global mobil und kommt aus allen Teilen der Welt.
Das PROBLEM MEINER ZIELGRUPPE:
Trotz hervorragender Fähigkeiten scheitert meine Zielgruppe im normalen Bewerbungsprozess. Der Grund: Sie werden nicht als individuelle Person, als Mensch mit Fähigkeiten bewertet - sondern nur als STEREOTYP gesehen. Ich helfe meinen Klienten in ein direktes Gespräch mit den Entscheidern einzutreten - damit sie wieder als einzelner Mensch, als Profi bewertet werden.
Aufgabenstellung
UPDATE: Ich habe ein neues Foto für die Rückseite hochgeladen. Morgen (Donnerstag) sende ich die verschiedenen Entwürfe zum Voting an meine Zielgruppe. Ich hoffe das ich dann innerhalb weniger Tage die Siegerin oder den Sieger bestimmen kann. :)
Aktualisierte Neuauflage meines englischsprachigen Buches 'Pathways to Hire & Charm the Locals'. Buchumschlag design für Verlora BPX Paperback und Hardcover.
Beide Formate sind in den Abmessungen identisch:
Paperback 13,97 x 21,59 cm
Hardcover 13,97 x 21,59 cm
UPDATE: Das Buch hat 159 Seiten.
Die 'Third updated Edition' sollte evtl. in einem Störer hervorgehoben werden.
Das Design muss aus der Masse der Verlora Titel hervorstechen - auch dann wenn man es auf einem Smartphone betrachtet. Das Design soll klar und modern sein. Ich prüfe bei jedem Design ob es zwischen diesen Suchresultaten auffallen würde:
https://www.verlora-shop.de/gp/toplist/books/582913/ref=vx_tl_qrbs_books
Würde ich dieses Buchcover anklicken?
Meine Zielgruppe verdient oberhalb von 60.000€ jährlich. Meine Dienstleistung (Coaching) ist entsprechend teuer. Am Besten denken Designer darüber nach wie über ein *Luxusprodukt* - dass dem Kunden aber gleichzeitig ein höheres Einkommen sichert.
Buchtitel: Pathways to Hire & Charm the Locals
Untertitel: The Newcomers' Manual for Working Abroad Well
Störer oder Teil des Untertitels: Third & Updated Edition
Author: Dana Owerk
Das Verlagslogo füge ich unten in zwei Versionen bei.
WICHTIG: Der Buchumschlag muss allen Verlora BPX Anforderungen entsprechen. (Z.B. Platz für barcode auf der Rückseite etc.) - Designs die diesen Anforderungen nicht entsprechen, scheiden automatisch aus.
Ansonsten habe ich keine Vorgaben.
Weitere Infos:
Klappentext - Rückseite:
German angst rules HR departments and destroys career opportunities for international talent and everyone else who dar..

```html
<!DOCTYPE html>
<html lang="en">
<head>
<meta charset="utf-8">
<title>Pathways to Hire &amp; Charm the Locals — Book Cover</title>
<link href="https://fonts.googleapis.com/css2?family=Oswald:wght@400;500;600&display=swap" rel="stylesheet">
<style>
  :root {
    --backdrop: #e6e6e6;
    --cover-black: #0c0c0c;
    --gold: #e3ad2c;
    --gold-deep: #b9801a;
    --white: #ffffff;
    --rule: #f2f2f2;
  }
  * { box-sizing: border-box; margin: 0; padding: 0; }
  html, body {
    width: 1200px; height: 1200px; overflow: hidden;
    background: var(--backdrop);
  }
  .stage { position: relative; width: 1200px; height: 1200px; }
  .cover {
    position: absolute; left: 243px; top: 100px;
    width: 687px; height: 998px;
    background: var(--cover-black);
    overflow: hidden;
    font-family: "Oswald", "Arial Narrow", sans-serif;
    color: var(--white);
  }
  .cover-art {
    position: absolute; left: 40px; top: 30px; width: 607px; height: 380px;
    background:
      radial-gradient(ellipse 22% 38% at 50% 88%, rgba(255,214,140,0.85), rgba(227,173,44,0.35) 45%, rgba(0,0,0,0) 100%),
      radial-gradient(ellipse 50% 55% at 50% 60%, rgba(185,128,26,0.28), rgba(0,0,0,0) 100%);
  }
  .edition-band { position: absolute; inset: 0; width: 687px; height: 998px; pointer-events: none; }
  .edition-text {
    font-family: "Oswald", "Arial Narrow", sans-serif;
    font-weight: 500; font-size: 17px; letter-spacing: 0.5px; fill: var(--cover-black);
  }
  .publisher {
    position: absolute; right: 14px; top: 30px;
    display: flex; align-items: center; gap: 4px;
    font-weight: 500; font-size: 14px; color: var(--gold);
  }
  .publisher .dot { width: 10px; height: 10px; border-radius: 50%; background: var(--gold); }
  .title-lead {
    position: absolute; left: 80px; width: 524px; top: 432px;
    display: flex; align-items: center; gap: 16px;
    font-weight: 500; font-size: 42px; line-height: 1; letter-spacing: 0.5px;
  }
  .title-lead .rule { flex: 1; height: 3px; background: var(--rule); }
  .title-big {
    position: absolute; left: 0; width: 100%; text-align: center;
    color: var(--gold); font-weight: 500; line-height: 1;
  }
  .title-hire { top: 486px; font-size: 136px; letter-spacing: 2px; }
  .title-amp {
    position: absolute; left: 0; width: 100%; text-align: center; top: 696px;
    font-weight: 500; font-size: 40px; line-height: 1;
  }
  .title-charm { top: 744px; font-size: 78px; letter-spacing: 1px; }
  .divider { position: absolute; left: 80px; width: 524px; height: 3px; background: var(--rule); }
  .divider-top { top: 689px; }
  .divider-mid { top: 848px; }
  .divider-bottom { top: 900px; height: 2px; }
  .subtitle {
    position: absolute; left: 0; width: 100%; top: 861px; text-align: center;
    font-weight: 400; font-size: 19px; letter-spacing: 1px; line-height: 1;
  }
  .author {
    position: absolute; left: 0; width: 100%; top: 920px; text-align: center;
    color: var(--gold); font-weight: 400; font-size: 34px; letter-spacing: 2px; line-height: 1;
  }
</style>
</head>
<body>
<div class="stage">
  <div class="cover">
    <div class="cover-art" role="img" aria-label="Illustration of many golden arrows rising upward from a glowing horizon, one tall arrow leading in the centre"></div>

    <svg class="edition-band" viewBox="0 0 687 998" aria-hidden="false">
      <polygon points="462,0 555,0 687,95 687,162" fill="var(--gold)"/>
      <text class="edition-text" x="0" y="0" text-anchor="middle" transform="translate(574,72) rotate(35.8)">THIRD &amp; UPDATED EDITION</text>
    </svg>

    <div class="publisher"><span class="dot"></span>Ardo</div>

    <div class="title-lead"><span class="rule"></span><span>PATHWAYS TO</span><span class="rule"></span></div>
    <div class="title-big title-hire">HIRE</div>
    <div class="divider divider-top"></div>
    <div class="title-amp">&amp;</div>
    <div class="title-big title-charm">CHARM THE LOCALS</div>
    <div class="divider divider-mid"></div>
    <div class="subtitle">THE NEWCOMERS' MANUAL FOR WORKING ABROAD WELL</div>
    <div class="divider divider-bottom"></div>
    <div class="author">DANA OWERK</div>
  </div>
</div>
</body>
</html>
```